Brindlewood Exteriors

Design 2-3 branded image ads using all for provided logos. each ad is for a roof replacement. The offer is, buy a new roof and receive a free gutter replacement, and 10 years of free rood maintenance. These must be included. What's optional ? you have the option the mention 50 year warranty, 25 year workmanship warranty. You also have an option to use price offer of $17,997.

```html
<!DOCTYPE html>
<html lang="en">
<head>
<meta charset="utf-8">
<title>Brindlewood Exteriors – Roof Replacement Ads</title>
<link rel="stylesheet" href="https://fonts.googleapis.com/css2?family=Bebas+Neue&family=Lexend:wght@400;500&family=Krona+One&family=Montserrat:wght@800&display=swap">
<style>
  :root {
    --board: #ededed;
    --sky-light: #2fd3ff;
    --sky-mid: #1a6fe8;
    --royal: #0b3fc4;
    --navy: #001a66;
    --green: #4ccf1c;
    --green-dark: #2e9e0b;
    --white: #ffffff;
    --partner-slot: rgba(255,255,255,.85);
    --house-wood: #b98a55;
    --house-roof: #2b3038;
    --text-dark: #061a06;
  }
  * { box-sizing: border-box; margin: 0; padding: 0; }
  html, body { width: 1200px; height: 838px; overflow: hidden; background: var(--board); }
  .board { position: relative; width: 1200px; height: 838px; }

  .ad { position: absolute; overflow: hidden; color: var(--white); font-family: "Lexend", sans-serif; }
  .ad--landscape {
    left: 119px; top: 241px; width: 625px; height: 334px;
    background:
      radial-gradient(ellipse 60% 70% at 8% 5%, var(--sky-light) 0%, rgba(47,211,255,0) 70%),
      radial-gradient(ellipse 40% 35% at 15% 90%, rgba(210,230,255,.75) 0%, rgba(210,230,255,0) 80%),
      linear-gradient(120deg, var(--sky-mid) 0%, var(--royal) 45%, var(--navy) 100%);
  }
  .ad--portrait {
    left: 786px; top: 88px; width: 321px; height: 662px;
    background:
      radial-gradient(ellipse 70% 20% at 90% 14%, rgba(47,211,255,.7) 0%, rgba(47,211,255,0) 80%),
      radial-gradient(ellipse 80% 18% at 50% 62%, rgba(190,215,255,.55) 0%, rgba(190,215,255,0) 80%),
      linear-gradient(180deg, var(--royal) 0%, var(--sky-mid) 35%, #2a74ea 60%, var(--royal) 80%, var(--navy) 100%);
  }

  /* Partner strip */
  .partner-tab { position: absolute; }
  .partner-tab > svg { position: absolute; inset: 0; width: 100%; height: 100%; }
  .partner-row { position: absolute; left: 0; right: 0; top: 16px; display: flex; align-items: center; justify-content: center; gap: 9px; }
  .brand-name { font-family: "Lexend", sans-serif; font-weight: 500; font-size: 7px; white-space: nowrap; color: var(--white); display: flex; align-items: center; gap: 3px; }
  .brand-name .dot { width: 6px; height: 6px; background: var(--white); }
  .partner-slot { width: 20px; height: 20px; border-radius: 50%; background: var(--partner-slot); }

  /* Offer shield */
  .shield { position: absolute; }
  .shield > svg { position: absolute; inset: 0; width: 100%; height: 100%; }
  .headline { position: absolute; left: 0; right: 0; text-align: center; font-family: "Bebas Neue", sans-serif; line-height: .95; color: var(--white); text-shadow: 1px 1px 0 var(--royal); }
  .amp-rule { position: absolute; display: flex; align-items: center; gap: 6px; font-family: "Lexend", sans-serif; font-weight: 500; color: var(--white); }
  .amp-rule::before, .amp-rule::after { content: ""; flex: 1; height: 1.5px; background: var(--white); }
  .years { position: absolute; left: 0; right: 0; text-align: center; font-family: "Bebas Neue", sans-serif; line-height: 1; color: var(--white); text-shadow: 3px 2px 0 var(--royal), 4px 3px 0 var(--navy); }
  .maintenance { position: absolute; left: 0; right: 0; text-align: center; font-weight: 500; color: var(--white); text-shadow: 1px 1px 0 var(--navy); }

  /* Warranty & price */
  .option-line { position: absolute; font-weight: 500; color: var(--white); white-space: nowrap; }
  .rule { position: absolute; height: 1px; background: rgba(255,255,255,.75); }
  .divider { position: absolute; width: 1px; background: rgba(255,255,255,.75); }
  .stat { position: absolute; }
  .stat-num { font-family: "Krona One", sans-serif; color: var(--green); line-height: 1; letter-spacing: -1px; }
  .stat-unit { position: absolute; top: -3px; font-weight: 400; color: var(--white); }
  .stat-label { position: absolute; white-space: nowrap; color: var(--white); font-weight: 400; }
  .tick { position: absolute; }
  .price-note { position: absolute; white-space: nowrap; color: var(--white); font-weight: 400; }
  .price { position: absolute; font-family: "Krona One", sans-serif; color: var(--white); line-height: 1; white-space: nowrap; letter-spacing: -1px; }
  .price sup { font-size: .4em; color: var(--green); vertical-align: top; position: relative; top: .1em; margin-right: 4px; }

  .cta { position: absolute; display: flex; align-items: center; justify-content: center; border-radius: 999px; background: linear-gradient(180deg, #6fe23b 0%, var(--green) 50%, var(--green-dark) 100%); font-family: "Montserrat", sans-serif; font-weight: 800; color: var(--text-dark); letter-spacing: -.5px; box-shadow: 0 2px 4px rgba(0,0,40,.35); }
</style>
</head>
<body>
<main class="board">

  <!-- Landscape ad -->
  <section class="ad ad--landscape" aria-label="Roof replacement offer, landscape">
    <div class="shield" style="left:31px;top:12px;width:250px;height:313px;">
      <svg viewBox="0 0 250 313" preserveAspectRatio="none">
        <defs>
          <linearGradient id="shieldFillA" x1="0" y1="0" x2="0" y2="1">
            <stop offset="0" stop-color="#3a8cff" stop-opacity=".35"/>
            <stop offset="1" stop-color="#ffffff" stop-opacity=".2"/>
          </linearGradient>
          <linearGradient id="houseA" x1="0" y1="0" x2="0" y2="1">
            <stop offset="0" stop-color="#2b3038"/>
            <stop offset=".45" stop-color="#2b3038"/>
            <stop offset=".55" stop-color="#b98a55"/>
            <stop offset="1" stop-color="#d8b27c"/>
          </linearGradient>
          <clipPath id="shieldClipA">
            <path d="M2,12 L125,2 L248,12 L248,175 C248,245 185,280 125,311 C65,280 2,245 2,175 Z"/>
          </clipPath>
        </defs>
        <path d="M2,12 L125,2 L248,12 L248,175 C248,245 185,280 125,311 C65,280 2,245 2,175 Z" fill="url(#shieldFillA)" stroke="#ffffff" stroke-width="3"/>
        <g role="img" aria-label="Photo of a modern timber house with a dark metal roof" clip-path="url(#shieldClipA)">
          <rect x="14" y="168" width="222" height="140" fill="url(#houseA)"/>
        </g>
      </svg>
      <div class="headline" style="top:22px;font-size:25px;">Buy a new roof and receive<br>a free gutter replacement</div>
      <div class="amp-rule" style="left:14px;right:14px;top:70px;font-size:14px;">&amp;</div>
      <div class="years" style="top:80px;font-size:76px;">10 Years</div>
      <div class="maintenance" style="top:147px;font-size:16px;">of free rood maintenance</div>
    </div>

    <div class="partner-tab" style="left:360px;top:0;width:179px;height:65px;">
      <svg viewBox="0 0 179 65" preserveAspectRatio="none" aria-hidden="true">
        <path d="M0,0 H179 V65 L89.5,53 L0,62 Z" fill="var(--green)"/>
      </svg>
      <div class="partner-row">
        <span class="brand-name"><span class="dot"></span>Brindlewood Exteriors</span>
        <span class="partner-slot"></span>
        <span class="partner-slot"></span>
        <span class="partner-slot"></span>
      </div>
    </div>

    <p class="option-line" style="left:311px;top:81px;font-size:17.5px;">you have the option the mention</p>
    <div class="rule" style="left:311px;width:280px;top:106px;"></div>

    <div class="stat" style="left:311px;top:116px;">
      <div class="stat-num" style="font-size:36px;">50</div>
      <span class="stat-unit" style="left:66px;font-size:12px;">year</span>
      <span class="stat-label" style="left:2px;top:39px;font-size:12px;">warranty</span>
    </div>
    <svg class="tick" style="left:385px;top:131px;" width="32" height="26" viewBox="0 0 32 26" aria-hidden="true"><path d="M3,13 L12,22 L29,3" fill="none" stroke="var(--green)" stroke-width="4.5" stroke-linecap="round"/></svg>
    <div class="divider" style="left:430px;top:109px;height:58px;"></div>
    <div class="stat" style="left:451px;top:116px;">
      <div class="stat-num" style="font-size:36px;">25</div>
      <span class="stat-unit" style="left:66px;font-size:12px;">year</span>
      <span class="stat-label" style="left:0;top:39px;font-size:12px;">workmanship warranty</span>
    </div>
    <svg class="tick" style="left:559px;top:113px;" width="32" height="26" viewBox="0 0 32 26" aria-hidden="true"><path d="M3,13 L12,22 L29,3" fill="none" stroke="var(--green)" stroke-width="4.5" stroke-linecap="round"/></svg>
    <div class="rule" style="left:311px;width:280px;top:169px;"></div>

    <p class="price-note" style="left:311px;top:175px;font-size:13.3px;">You also have an option to use price of fer of</p>
    <p class="price" style="left:311px;top:195px;font-size:58px;"><sup>$</sup>17,997</p>

    <a class="cta" style="left:367px;top:276px;width:166px;height:35px;font-size:18px;">BOOK A CALL</a>
  </section>

  <!-- Portrait ad -->
  <section class="ad ad--portrait" aria-label="Roof replacement offer, portrait">
    <div class="partner-tab" style="left:72px;top:0;width:178px;height:64px;">
      <svg viewBox="0 0 178 64" preserveAspectRatio="none" aria-hidden="true">
        <path d="M0,0 H178 V64 L89,56 L0,64 Z" fill="var(--green)"/>
      </svg>
      <div class="partner-row" style="top:16px;">
        <span class="brand-name"><span class="dot"></span>Brindlewood Exteriors</span>
        <span class="partner-slot"></span>
        <span class="partner-slot"></span>
        <span class="partner-slot"></span>
      </div>
    </div>

    <div class="shield" style="left:26px;top:81px;width:270px;height:337px;">
      <svg viewBox="0 0 270 337" preserveAspectRatio="none">
        <defs>
          <linearGradient id="shieldFillB" x1="0" y1="0" x2="0" y2="1">
            <stop offset="0" stop-color="#2fd3ff" stop-opacity=".55"/>
            <stop offset="1" stop-color="#ffffff" stop-opacity=".2"/>
          </linearGradient>
          <linearGradient id="houseB" x1="0" y1="0" x2="0" y2="1">
            <stop offset="0" stop-color="#2b3038"/>
            <stop offset=".45" stop-color="#2b3038"/>
            <stop offset=".55" stop-color="#b98a55"/>
            <stop offset="1" stop-color="#d8b27c"/>
          </linearGradient>
          <clipPath id="shieldClipB">
            <path d="M2,12 L135,2 L268,12 L268,190 C268,265 200,300 135,335 C70,300 2,265 2,190 Z"/>
          </clipPath>
        </defs>
        <path d="M2,12 L135,2 L268,12 L268,190 C268,265 200,300 135,335 C70,300 2,265 2,190 Z" fill="url(#shieldFillB)" stroke="#ffffff" stroke-width="3"/>
        <g role="img" aria-label="Photo of a modern timber house with a dark metal roof" clip-path="url(#shieldClipB)">
          <rect x="14" y="176" width="242" height="156" fill="url(#houseB)"/>
        </g>
      </svg>
      <div class="headline" style="top:24px;font-size:27px;">Buy a new roof and receive<br>a free gutter replacement</div>
      <div class="amp-rule" style="left:16px;right:16px;top:73px;font-size:15px;">&amp;</div>
      <div class="years" style="top:82px;font-size:82px;">10 Years</div>
      <div class="maintenance" style="top:155px;font-size:17px;">of free rood maintenance</div>
    </div>

    <a class="cta" style="left:78px;top:437px;width:165px;height:37px;font-size:18px;">BOOK A CALL</a>

    <p class="option-line" style="left:33px;top:480px;font-size:16.5px;">you have the option the mention</p>
    <div class="rule" style="left:33px;width:258px;top:503px;"></div>
    <div class="stat" style="left:33px;top:513px;">
      <div class="stat-num" style="font-size:33px;">50</div>
      <span class="stat-unit" style="left:61px;font-size:11.5px;">year</span>
      <span class="stat-label" style="left:1px;top:35px;font-size:11.5px;">warranty</span>
    </div>
    <svg class="tick" style="left:101px;top:527px;" width="30" height="24" viewBox="0 0 32 26" aria-hidden="true"><path d="M3,13 L12,22 L29,3" fill="none" stroke="var(--green)" stroke-width="4.5" stroke-linecap="round"/></svg>
    <div class="divider" style="left:145px;top:506px;height:55px;"></div>
    <div class="stat" style="left:160px;top:513px;">
      <div class="stat-num" style="font-size:33px;">25</div>
      <span class="stat-unit" style="left:59px;font-size:11.5px;">year</span>
      <span class="stat-label" style="left:0;top:35px;font-size:11.5px;">workmanship warranty</span>
    </div>
    <svg class="tick" style="left:260px;top:512px;" width="30" height="24" viewBox="0 0 32 26" aria-hidden="true"><path d="M3,13 L12,22 L29,3" fill="none" stroke="var(--green)" stroke-width="4.5" stroke-linecap="round"/></svg>
    <div class="rule" style="left:33px;width:258px;top:564px;"></div>

    <p class="price-note" style="left:33px;top:569px;font-size:12.3px;">You also have an option to use price of fer of</p>
    <p class="price" style="left:33px;top:588px;font-size:54px;"><sup>$</sup>17,997</p>
  </section>

</main>
</body>
</html>
```